Creative Agency Showcase/Profile

Looking for a impactful, clean design to showcase our best works.

Our events company: www.bramblequillstudios.com.sg

We have a clean and impactful look which we want to maintain. Looking at how we can best showcase our works/events to new customers who we want to do business with.

Actual photos will be provided once appointed.

Target Market(s)

Corporates, New Customers

Font styles to use
Sans Serif

Colors
ec1f27
0592cd
f78f20
6b439b
ffffff

Requirements
Must have
• Key Tagline:
• BREAKING NEW GROUND
• To be presented on a 16:9 Landscape format (prefably editable in KEYNOTE in the future)
• Total should be at least 8-10 pages including a COVER PAGE and CONTACT US PAGE.
Nice to have
• Some secondary captions/by lines.
• Must include event pictures.
• Hoping to have one picture per slide.
• Please use stock images at least 8-10 for now.

```html
<!DOCTYPE html>
<html lang="en">
<head>
<meta charset="utf-8">
<title>Bramblequill Studios – Profile Deck Layouts</title>
<link rel="stylesheet" href="https://fonts.googleapis.com/css2?family=Oswald:wght@400;500&family=Open+Sans:wght@400;600;700&display=swap">
<style>
:root{
  --red:#d0141c;
  --red-soft:#e0454b;
  --black:#0d0d0d;
  --white:#ffffff;
  --paper:#f7f7f8;
  --grey:#dcdcdc;
  --board:#58595b;
  --muted:#8a8a8a;
}
*{box-sizing:border-box;margin:0;padding:0}
html,body{width:1200px;height:581px;overflow:hidden;background:var(--board)}
body{position:relative;font-family:"Open Sans",Arial,sans-serif;color:var(--black)}
.slide{position:absolute;width:274px;height:165px;background:var(--paper);overflow:hidden}
.abs{position:absolute}
.top-stripe{position:absolute;left:0;top:0;width:274px;height:6px}
.title{position:absolute;font-weight:700;font-size:9.5px;line-height:11px;letter-spacing:-.2px}
.tiny{position:absolute;font-size:3.2px;line-height:4.2px}
.body{position:absolute;font-weight:700;font-size:6.4px;line-height:8px}
.white{color:var(--white)}
.redtxt{color:var(--red)}
.photo{position:absolute;inset:0}
.cam{position:absolute;text-align:center;color:var(--white);font-size:4.6px;line-height:5.4px}
.cam svg{display:block;margin:0 auto 2px}
</style>
</head>
<body>

<!-- Cover -->
<section class="slide cover" style="left:30px;top:27px">
  <div class="photo" role="img" aria-label="Event photo of a crowd celebrating at a night party with red stage lighting" style="background:radial-gradient(circle at 75% 60%,#c9624e 0%,#6b2a25 40%,#2a1213 100%)"></div>
  <svg class="abs" style="left:0;top:0" width="274" height="165">
    <polygon points="0,0 150,0 205,50 120,165 0,165" fill="var(--red)" opacity=".88"/>
    <polygon points="60,0 150,0 205,50 160,110" fill="var(--red-soft)" opacity=".5"/>
  </svg>
  <div class="abs white" style="left:15px;top:72px;font-family:Oswald,sans-serif;font-weight:500;font-size:16px;line-height:19px">WELCOME</div>
  <div class="abs white" style="left:15px;top:95px;font-family:Oswald,sans-serif;font-weight:500;font-size:18.5px;line-height:19.5px">EVENT COMPANY<br>IN SINGAPORE</div>
  <div class="abs" style="left:200px;top:88px;width:28px;height:28px;border:2.5px solid var(--white);border-radius:50%"></div>
  <div class="abs white" style="left:182px;top:119px;width:66px;text-align:center;font-family:Oswald,sans-serif;font-weight:500;font-size:7.4px;line-height:8px">BRAMBLEQUILL<br>STUDIOS</div>
</section>

<!-- Services icons -->
<section class="slide services" style="left:320px;top:27px">
  <div class="photo" role="img" aria-label="Faded photo of an event hall" style="background:linear-gradient(180deg,#e9e9ea,#dadadb)"></div>
  <svg class="top-stripe"><polygon points="20,0 135,0 130,6 15,6" fill="var(--black)"/><polygon points="130,0 260,0 255,6 125,6" fill="var(--red)"/></svg>
  <div class="title" style="left:20px;top:30px">Lorem ipsum dolor<br>sit amet</div>
  <svg class="abs" style="left:0;top:0" width="274" height="165">
    <g>
      <circle cx="30" cy="62" r="7" fill="var(--black)"/><circle cx="114" cy="62" r="7" fill="var(--red)"/><circle cx="201" cy="62" r="7" fill="var(--black)"/>
      <circle cx="30" cy="100" r="7" fill="var(--red)"/><circle cx="114" cy="100" r="7" fill="var(--black)"/><circle cx="201" cy="100" r="7" fill="var(--red)"/>
    </g>
    <g fill="none" stroke="var(--white)" stroke-width=".8">
      <circle cx="30" cy="60.5" r="1.8"/><path d="M26.5 66a3.5 3 0 0 1 7 0"/>
      <circle cx="114" cy="60.5" r="1.8"/><path d="M110.5 66a3.5 3 0 0 1 7 0"/>
      <circle cx="201" cy="60.5" r="1.8"/><path d="M197.5 66a3.5 3 0 0 1 7 0"/>
      <circle cx="30" cy="98.5" r="1.8"/><path d="M26.5 104a3.5 3 0 0 1 7 0"/>
      <circle cx="114" cy="98.5" r="1.8"/><path d="M110.5 104a3.5 3 0 0 1 7 0"/>
      <circle cx="201" cy="98.5" r="1.8"/><path d="M197.5 104a3.5 3 0 0 1 7 0"/>
    </g>
    <g stroke="var(--black)" stroke-width=".6">
      <line x1="42" y1="54" x2="42" y2="70"/><line x1="126" y1="54" x2="126" y2="70"/><line x1="213" y1="54" x2="213" y2="70"/>
      <line x1="42" y1="92" x2="42" y2="108"/><line x1="126" y1="92" x2="126" y2="108"/><line x1="213" y1="92" x2="213" y2="108"/>
    </g>
  </svg>
  <div class="tiny" style="left:46px;top:55px;width:50px"><b>Lorem ipsum</b><br>Dummy text of the printing and typesetting industry.</div>
  <div class="tiny" style="left:130px;top:55px;width:50px"><b>Lorem ipsum</b><br>Dummy text of the printing and typesetting industry.</div>
  <div class="tiny" style="left:217px;top:55px;width:50px"><b>Lorem ipsum</b><br>Dummy text of the printing and typesetting industry.</div>
  <div class="tiny" style="left:46px;top:93px;width:50px"><b>Lorem ipsum</b><br>Dummy text of the printing and typesetting industry.</div>
  <div class="tiny" style="left:130px;top:93px;width:50px"><b>Lorem ipsum</b><br>Dummy text of the printing and typesetting industry.</div>
  <div class="tiny" style="left:217px;top:93px;width:50px"><b>Lorem ipsum</b><br>Dummy text of the printing and typesetting industry.</div>
  <div class="abs" style="left:22px;top:122px;width:233px;height:26px;background:var(--red)"></div>
  <div class="tiny white" style="left:26px;top:130px;width:220px">Lorem Ipsum is simply dummy text of the printing and typesetting industry. Lorem Ipsum has been the industry's standard dummy text ever since the 1500s, when an unknown printer took a galley of type.</div>
</section>

<!-- Statement -->
<section class="slide statement" style="left:608px;top:27px;background:var(--white)">
  <svg class="abs" style="left:16px;top:15px" width="243" height="134">
    <rect width="243" height="134" fill="var(--red)"/>
    <polygon points="0,0 60,0 200,134 0,134" fill="var(--red-soft)" opacity=".6"/>
  </svg>
  <div class="abs" style="left:34px;top:36px;font-weight:600;font-size:19px;line-height:21px;letter-spacing:-.5px">Lorem<br>ipsum<br>dolor<br>sit amet</div>
  <div class="abs" style="left:152px;top:50px;font-weight:700;font-size:7px;line-height:8px">Lorem ipsum dolor<br>sit amet</div>
  <div class="tiny white" style="left:152px;top:72px;width:92px">Lorem ipsum is simply dummy text of the printing and typesetting industry, standard since the 1500s.</div>
  <div class="tiny white" style="left:152px;top:92px;width:92px">An unknown printer took a galley of type and scrambled it to make a type specimen book.</div>
  <div class="tiny white" style="left:152px;top:110px;width:92px">It has survived five centuries and the leap into electronic typesetting.</div>
</section>

<!-- Venn diagram -->
<section class="slide venn" style="left:896px;top:27px;background:var(--white)">
  <svg class="top-stripe"><polygon points="110,0 170,0 165,6 105,6" fill="var(--grey)"/><polygon points="170,0 274,0 274,6 165,6" fill="var(--red)"/></svg>
  <div class="title" style="left:20px;top:18px">Lorem ipsum dolor<br>sit amet</div>
  <svg class="abs" style="left:0;top:0" width="274" height="165">
    <circle cx="84" cy="115" r="20" fill="var(--black)"/><circle cx="114" cy="115" r="20" fill="var(--black)"/>
    <circle cx="99" cy="100" r="20" fill="var(--black)"/>
    <circle cx="99" cy="85" r="20" fill="var(--red)"/>
    <g stroke="var(--muted)" stroke-width=".5" fill="none">
      <line x1="68" y1="63" x2="128" y2="63"/><line x1="99" y1="63" x2="99" y2="66"/>
      <polyline points="66,126 50,140 28,140"/><polyline points="131,126 145,140 170,140"/>
    </g>
    <circle cx="186" cy="81" r="4.5" fill="var(--red)"/><circle cx="186" cy="97" r="4.5" fill="var(--black)"/><circle cx="186" cy="113" r="4.5" fill="var(--black)"/>
  </svg>
  <div class="tiny" style="left:78px;top:55px"><b>Lorem ipsum dolor sit.</b></div>
  <div class="tiny" style="left:28px;top:142px;width:50px"><b>Lorem ipsum dolor sit.</b><br>Dummy text of the printing.</div>
  <div class="tiny" style="left:140px;top:142px;width:50px"><b>Lorem ipsum dolor sit.</b><br>Dummy text of the printing.</div>
  <div class="tiny" style="left:194px;top:79px;width:52px">Lorem ipsum is simply dummy text of print.</div>
  <div class="tiny" style="left:194px;top:95px;width:52px">Lorem ipsum is simply dummy text of print.</div>
  <div class="tiny" style="left:194px;top:111px;width:52px">Lorem ipsum is simply dummy text of print.</div>
</section>

<!-- Process circles -->
<section class="slide process" style="left:30px;top:207px;background:var(--white)">
  <svg class="top-stripe"><polygon points="20,0 160,0 155,6 15,6" fill="var(--grey)"/><polygon points="150,0 274,0 274,6 145,6" fill="var(--red)"/></svg>
  <div class="abs" style="left:0;width:274px;top:26px;text-align:center;font-size:13px;line-height:15px">Lorem ipsum dolor<br>sit amet</div>
  <svg class="abs" style="left:0;top:0" width="274" height="165">
    <g fill="none" stroke="var(--black)" stroke-width=".8">
      <circle cx="55" cy="99" r="26"/><circle cx="109" cy="99" r="26"/><circle cx="163" cy="99" r="26"/><circle cx="217" cy="99" r="26"/>
    </g>
    <circle cx="55" cy="99" r="22" fill="var(--red)"/><circle cx="109" cy="99" r="22" fill="var(--black)"/>
    <circle cx="163" cy="99" r="22" fill="var(--red)"/><circle cx="217" cy="99" r="22" fill="var(--black)"/>
    <g fill="var(--black)"><circle cx="82" cy="99" r="1.6"/><circle cx="136" cy="99" r="1.6"/><circle cx="190" cy="99" r="1.6"/></g>
    <g fill="none" stroke="var(--white)" stroke-width=".8">
      <circle cx="55" cy="89" r="3.5"/><line x1="53.5" y1="94" x2="56.5" y2="94"/>
      <circle cx="163" cy="90" r="4"/><polyline points="163,87.5 163,90 165,91"/>
    </g>
    <path d="M106 85h4.5l2 2v7h-6.5z" fill="var(--red)"/>
    <path d="M213 86h3l1 1h4v7h-8z" fill="var(--red)"/>
  </svg>
  <div class="tiny white" style="left:40px;top:102px;width:30px;text-align:center">Lorem ipsum dolor sit amet.</div>
  <div class="tiny white" style="left:94px;top:102px;width:30px;text-align:center">Lorem ipsum dolor sit amet.</div>
  <div class="tiny white" style="left:148px;top:102px;width:30px;text-align:center">Lorem ipsum dolor sit amet.</div>
  <div class="tiny white" style="left:202px;top:102px;width:30px;text-align:center">Lorem ipsum dolor sit amet.</div>
  <div class="tiny" style="left:40px;top:140px;width:200px">Lorem Ipsum is simply dummy text of the printing and typesetting industry. Lorem Ipsum has been the industry's standard dummy text ever since the 1500s, when a printer took a galley of type.</div>
</section>

<!-- Feature split -->
<section class="slide feature" style="left:320px;top:207px;background:var(--white)">
  <div class="abs" style="left:42px;top:0;width:150px;height:165px;background:var(--red)"></div>
  <div class="abs" style="left:192px;top:0;width:82px;height:165px;background:var(--black)"></div>
  <svg class="abs" style="left:120px;top:0" width="154" height="165"><line x1="33" y1="0" x2="33" y2="165" stroke="#e03a40" stroke-width=".5"/><circle cx="112" cy="62" r="46" fill="#ffffff" opacity=".05"/><circle cx="92" cy="130" r="30" fill="#ffffff" opacity=".05"/></svg>
  <div class="abs" style="left:56px;top:36px;font-weight:600;font-size:7.4px;line-height:9px">Lorem ipsum dolor<br>sit amet.</div>
  <div class="body white" style="left:56px;top:68px;width:100px">Lorem ipsum dolor sit amet, consectetur adipiscing elit, sed do eiusmod tempor incididunt ut labore et dolore magna aliqua.</div>
  <div class="cam" style="left:202px;top:68px;width:60px" role="img" aria-label="Event photo placeholder">
    <svg width="18" height="13" viewBox="0 0 18 13"><rect x=".6" y="2.6" width="16.8" height="9.8" rx="1" fill="none" stroke="#fff" stroke-width=".9"/><rect x="5" y=".6" width="5" height="2" fill="#fff"/><circle cx="9" cy="7.5" r="3" fill="none" stroke="#fff" stroke-width=".9"/></svg>
    Add your image<br>here
  </div>
</section>

<!-- Growth chart -->
<section class="slide growth" style="left:608px;top:207px;background:var(--white)">
  <svg class="top-stripe"><polygon points="20,0 130,0 125,6 15,6" fill="var(--grey)"/><polygon points="125,0 274,0 274,6 120,6" fill="var(--red)"/></svg>
  <svg class="abs" style="left:0;top:0" width="274" height="165">
    <g fill="#eeeeee"><rect x="32" y="40" width="112" height="12"/><rect x="32" y="64" width="112" height="12"/><rect x="32" y="88" width="112" height="12"/></g>
    <path d="M32 124 C70 118 95 110 115 96 L144 74 L144 124 Z" fill="var(--black)"/>
    <path d="M32 124 C70 121 95 118 115 110 L144 98 L144 124 Z" fill="var(--red)"/>
    <g stroke="var(--muted)" stroke-width=".4"><line x1="144" y1="40" x2="156" y2="40"/><line x1="144" y1="74" x2="156" y2="74"/><line x1="144" y1="98" x2="156" y2="98"/></g>
  </svg>
  <div class="tiny" style="left:158px;top:38px">25.00</div><div class="tiny" style="left:158px;top:72px">20.00</div><div class="tiny" style="left:158px;top:96px">15.00</div>
  <div class="tiny" style="left:32px;top:128px;width:118px;word-spacing:9px">0 5 10 15 20 25 30</div>
  <div class="abs" style="left:184px;top:40px;font-weight:700;font-size:5.6px">Lorem ipsum dolor sit amet.</div>
  <div class="tiny" style="left:184px;top:52px;width:76px"><b>Lorem Ipsum is simply dummy text of the printing and typesetting industry.</b> It has been the standard dummy text since the 1500s, when a printer scrambled type.</div>
  <div class="tiny" style="left:184px;top:78px;width:76px"><b>Lorem Ipsum is simply dummy text of the printing and typesetting industry.</b> It has survived five centuries and the leap into electronic typesetting, remaining unchanged.</div>
</section>

<!-- Hexagon list -->
<section class="slide hexlist" style="left:896px;top:207px;background:var(--white)">
  <div class="abs" style="left:134px;top:0;width:34px;height:165px;background:var(--red)"></div>
  <div class="abs" style="left:168px;top:0;width:82px;height:165px;background:var(--black)"></div>
  <div class="title" style="left:22px;top:40px">Lorem ipsum dolor<br>sit amet</div>
  <div class="tiny" style="left:22px;top:66px;width:100px">Lorem ipsum is simply dummy text of the printing and typesetting industry, the standard since the 1500s.</div>
  <div class="tiny" style="left:22px;top:84px;width:100px">An unknown printer took a galley of type and scrambled it to make a type specimen book.</div>
  <div class="tiny" style="left:22px;top:102px;width:100px">It has survived five centuries and the leap into electronic typesetting.</div>
  <svg class="abs" style="left:138px;top:0" width="26" height="165">
    <g fill="none" stroke="var(--black)" stroke-width=".9">
      <polygon points="13,40 23,45.5 23,56.5 13,62 3,56.5 3,45.5"/>
      <polygon points="13,73 23,78.5 23,89.5 13,95 3,89.5 3,78.5"/>
      <polygon points="13,106 23,111.5 23,122.5 13,128 3,122.5 3,111.5"/>
    </g>
    <path d="M9 48h3l1 1h4v6h-8z" fill="var(--black)"/>
    <circle cx="13" cy="84" r="3.6" fill="none" stroke="var(--black)" stroke-width=".8"/><path d="M13 84v-3.6a3.6 3.6 0 0 1 3.6 3.6z" fill="var(--black)"/>
    <path d="M10 113h4l2 2v6h-6z" fill="none" stroke="var(--black)" stroke-width=".8"/>
  </svg>
  <div class="tiny white" style="left:176px;top:40px;width:70px;font-size:4.2px;line-height:5.2px"><b>Lorem ipsum</b><br>Lorem Ipsum is simply dummy text of the printing and typesetting industry.</div>
  <div class="tiny white" style="left:176px;top:73px;width:70px;font-size:4.2px;line-height:5.2px"><b>Lorem ipsum</b><br>Lorem Ipsum is simply dummy text of the printing and typesetting industry.</div>
  <div class="tiny white" style="left:176px;top:106px;width:70px;font-size:4.2px;line-height:5.2px"><b>Lorem ipsum</b><br>Lorem Ipsum is simply dummy text of the printing and typesetting industry.</div>
</section>

<!-- Stats mosaic -->
<section class="slide stats" style="left:30px;top:387px;background:var(--white)">
  <div class="abs" style="left:46px;top:0;width:228px;height:84px;background:var(--black)"></div>
  <svg class="abs" style="left:46px;top:0" width="228" height="84"><circle cx="118" cy="92" r="30" fill="#fff" opacity=".05"/></svg>
  <div class="cam" style="left:60px;top:28px;width:60px" role="img" aria-label="Event photo placeholder">
    <svg width="20" height="14" viewBox="0 0 18 13"><rect x=".6" y="2.6" width="16.8" height="9.8" rx="1" fill="none" stroke="#fff" stroke-width=".9"/><rect x="5" y=".6" width="5" height="2" fill="#fff"/><circle cx="9" cy="7.5" r="3" fill="none" stroke="#fff" stroke-width=".9"/></svg>
    Add your image<br>here
  </div>
  <div class="body redtxt" style="left:168px;top:24px;width:100px">Lorem ipsum dolor sit amet, consectetur adipiscing elit, sed do eiusmod tempor incididunt ut labore et dolore magna aliqua.</div>
  <div class="abs" style="left:0;top:84px;width:168px;height:81px;background:var(--red)"></div>
  <div class="abs" style="left:14px;top:92px;font-weight:700;font-size:5.6px">Lorem ipsum dolor sit amet.</div>
  <svg class="abs" style="left:0;top:84px" width="168" height="81">
    <g fill="none" stroke-width="3">
      <circle cx="42" cy="40" r="13" stroke="#ffffff"/><path d="M42 27a13 13 0 1 1 -12.4 17" stroke="var(--black)"/>
      <circle cx="92" cy="40" r="13" stroke="#ffffff"/><path d="M92 27a13 13 0 1 1 -9 22.4" stroke="var(--black)"/>
      <circle cx="142" cy="40" r="13" stroke="#ffffff"/><path d="M142 27a13 13 0 1 1 -12 8" stroke="var(--black)"/>
    </g>
  </svg>
  <div class="tiny" style="left:32px;top:122px;width:20px;text-align:center;font-weight:700">Lorem ipsum</div>
  <div class="tiny" style="left:82px;top:122px;width:20px;text-align:center;font-weight:700">Lorem ipsum</div>
  <div class="tiny" style="left:132px;top:122px;width:20px;text-align:center;font-weight:700">Lorem ipsum</div>
  <div class="tiny" style="left:14px;top:150px;width:145px">Lorem Ipsum is simply dummy text of the printing and typesetting industry since the 1500s.</div>
  <div class="abs" style="left:182px;top:104px;font-weight:700;font-size:7px;line-height:8px">Lorem ipsum dolor<br>sit amet</div>
  <div class="tiny" style="left:182px;top:124px;width:82px">Lorem Ipsum is simply dummy text of the printing and typesetting industry. Lorem Ipsum has been the industry's standard dummy text ever since the 1500s, when a printer scrambled type.</div>
</section>

<!-- Bar and line chart -->
<section class="slide barchart" style="left:320px;top:387px;background:var(--white)">
  <svg class="top-stripe"><polygon points="20,0 140,0 135,6 15,6" fill="var(--grey)"/><polygon points="135,0 274,0 274,6 130,6" fill="var(--red)"/></svg>
  <div class="title" style="left:18px;top:30px">Lorem ipsum dolor<br>sit amet</div>
  <svg class="abs" style="left:0;top:0" width="274" height="165">
    <g stroke="#e3e3e3" stroke-width=".4"><line x1="26" y1="80" x2="158" y2="80"/><line x1="26" y1="88" x2="158" y2="88"/><line x1="26" y1="96" x2="158" y2="96"/><line x1="26" y1="104" x2="158" y2="104"/><line x1="26" y1="112" x2="158" y2="112"/><line x1="26" y1="120" x2="158" y2="120"/></g>
    <g fill="var(--red)"><rect x="30" y="104" width="3" height="24"/><rect x="66" y="84" width="3" height="44"/><rect x="102" y="92" width="3" height="36"/><rect x="136" y="96" width="3" height="32"/></g>
    <g fill="var(--black)"><rect x="48" y="94" width="3" height="34"/><rect x="84" y="90" width="3" height="38"/><rect x="118" y="94" width="3" height="34"/></g>
    <polyline points="31,102 49,90 67,80 85,88 103,90 119,92 137,94 156,98" fill="none" stroke="var(--black)" stroke-width=".6"/>
    <polyline points="31,108 49,96 67,86 85,94 103,96 119,98 137,100 156,102" fill="none" stroke="var(--red)" stroke-width=".6"/>
    <g fill="var(--black)"><circle cx="49" cy="90" r=".9"/><circle cx="67" cy="80" r=".9"/><circle cx="85" cy="88" r=".9"/><circle cx="103" cy="90" r=".9"/><circle cx="119" cy="92" r=".9"/><circle cx="137" cy="94" r=".9"/></g>
  </svg>
  <div class="tiny" style="left:18px;top:140px;width:140px">Lorem Ipsum is simply dummy text of the printing and typesetting industry. Lorem Ipsum has been the industry's standard dummy text ever since the 1500s, when a printer took a galley of type.</div>
  <div class="abs" style="left:170px;top:39px;width:104px;height:98px;border:1.2px solid var(--red);border-right:none"></div>
  <div class="abs" style="left:181px;top:58px;font-weight:700;font-size:5.6px;line-height:6.6px">Lorem ipsum dolor<br>sit amet</div>
  <div class="abs" style="left:181px;top:76px;width:86px;font-weight:600;font-size:5.4px;line-height:7px">Lorem ipsum dolor sit amet, consectetur adipiscing elit, sed do eiusmod tempor incididunt ut labore et dolore magna aliqua.</div>
</section>

<!-- Diagonal feature -->
<section class="slide diagonal" style="left:608px;top:387px;background:var(--white)">
  <svg class="abs" style="left:0;top:0" width="274" height="165">
    <polygon points="82,0 274,0 274,4 190,165 0,165 0,62" fill="var(--red)"/>
    <polygon points="274,4 274,165 190,165" fill="var(--black)"/>
    <circle cx="215" cy="118" r="24" fill="#fff" opacity=".05"/>
  </svg>
  <div class="abs" style="left:28px;top:54px;font-weight:600;font-size:7.4px;line-height:8.6px">Lorem ipsum dolor<br>sit amet</div>
  <div class="abs white" style="left:28px;top:82px;width:110px;font-weight:600;font-size:7.2px;line-height:9.4px">Lorem ipsum dolor sit amet, consectetur adipiscing elit, sed do eiusmod tempor incididunt ut labore et dolore magna aliqua.</div>
  <div class="cam" style="left:202px;top:103px;width:54px" role="img" aria-label="Event photo placeholder">
    <svg width="18" height="13" viewBox="0 0 18 13"><rect x=".6" y="2.6" width="16.8" height="9.8" rx="1" fill="none" stroke="#fff" stroke-width=".9"/><rect x="5" y=".6" width="5" height="2" fill="#fff"/><circle cx="9" cy="7.5" r="3" fill="none" stroke="#fff" stroke-width=".9"/></svg>
    Add your image<br>here
  </div>
</section>

<!-- Contact -->
<section class="slide contact" style="left:896px;top:387px;background:var(--white)">
  <div class="abs" style="left:40px;top:24px;width:168px;height:117px;border:1.5px solid var(--red)"></div>
  <div class="abs" style="left:58px;top:46px;font-weight:700;font-size:7.4px;line-height:8.6px">Lorem ipsum dolor<br>sit amet</div>
  <div class="abs" style="left:58px;top:72px;width:104px;font-weight:600;font-size:6.4px;line-height:8.2px">Lorem ipsum dolor sit amet, consectetur adipiscing elit, sed do eiusmod tempor incididunt ut labore et dolore magna aliqua.</div>
  <div class="abs" style="left:178px;top:45px;width:58px;height:76px;background:var(--black)"></div>
  <svg class="abs" style="left:178px;top:45px" width="58" height="76">
    <g fill="none" stroke="var(--red)" stroke-width=".7">
      <rect x="6" y="6" width="5" height="8" rx=".6"/>
      <rect x="5" y="29" width="7" height="5"/><polyline points="5,29 8.5,32 12,29"/>
      <rect x="5" y="52" width="7" height="5"/><line x1="7" y1="59" x2="10" y2="59"/>
    </g>
    <g stroke="var(--red)" stroke-width=".4" stroke-dasharray="1 .8"><line x1="4" y1="22" x2="54" y2="22"/><line x1="4" y1="45" x2="54" y2="45"/></g>
  </svg>
  <div class="tiny white" style="left:192px;top:50px;width:40px;font-size:3px;line-height:3.8px">+65 6000 1234<br>Call us any weekday.</div>
  <div class="tiny white" style="left:192px;top:73px;width:40px;font-size:3px;line-height:3.8px">hello@bramblequill<br>studios.com.sg</div>
  <div class="tiny white" style="left:192px;top:96px;width:40px;font-size:3px;line-height:3.8px">www.bramblequillstudios<br>.com.sg</div>
</section>

</body>
</html>
```